Web-page design

We need a initial web design for our page kavilora.com.au (which is not yet set up).
We provide consulting services for all kinds of problems in and between organisations.
Main focus is on conflict resolution but we also support companies on improving their operational performance.
We want to have the following page structure (and part of the project is to design the 8 pages):
- Home
- Services (we offer 3 main service areas - one per page)
- Case studies (one per page)
- Engaging us (our process)
- About Conflict & low performance
- Conflict resolution App
- About
- Contact (Email form)
- Our logo should be on each page.
The start page should include the following information:
- Twitter / Linkedin / facebook/ google + Links
- Telephone / Email or in general contact details
- News
- A quite prominent picture box with 3 alternating pics - each representing one of our service areas
- Link to our App
- Testimonials
It would be nice if the service pages would have an image header. Links to the information section (about conflict & low performance; and the app page) would be nice as well.
We like the following joomla designs: www.quorbixlane.com/itempreview/153
No need to copy it, it should just give you an idea.
We like the layout here with the picture and space for the case studies on the left. Somewhere beneath should be the 3 service areas with a picture each.
In terms of colors: our logo colours are Blue (RBG 8;44;80) and Orange (RGB 231;120;23). The orange could be used to emphasise certain things, however there should not be too much color.
Budget for images available, so please use placeholders or ask us for specific photos/images, if you need them for your design.
Updates
Hi, one more thing that we would like to have is the case studies not hidden behind a link "case studies" - we would like to have them individually linked prominent on the first page. There will be about 6-8 of them. Thats what we liked on the joomla template (the links left from the picture).
Hi, thanks very much for all the great proposals.
We are currently going through the selection process and will post our decision early next week.
Thanks again!
Liesel
Target Market(s)
- target customers are all different kinds of businesses and organisations (all industries, government, non-for-profit, ...) experiencing conflict and tension - be it with internal staff, amongst managers or board members, dysfunctional teams, between organizations or customers and organizations... examples could be bullying allegations, governmental negotiations with unions, disputes within organizations etc.
- also we will offer performance improvement services for organizations
- we will offer mediation, facilitation, negotiation, performance improvement services, conflict coaching, conflict management, change management services
- if comparable to anything - then to a law firm in terms of dealing with conflicts but its much less adversarial and much more about the people and their interests rather than about laws
- basically it's all kind of things you can do in order to solve disputes without involving lawyers and a court - so it's much cheaper and target is to find a solution all parties can live with rather than having a judge deciding about who wins and who looses
- performance management is more about analysing reasons for a lack of performance and setting up continous improvement systems, supporting change management, facilitating improvement workshops or strategic meetings, ...
Industry/Entity Type
Consulting
Look and feel

```html
<!DOCTYPE html>
<html lang="en">
<head>
<meta charset="utf-8">
<title>Marlow Tessing – Conflict Resolution Consulting</title>
<link href="https://fonts.googleapis.com/css2?family=Source+Sans+3:wght@400;600&family=Ubuntu:wght@400;500&family=Arimo:wght@400;700&display=swap" rel="stylesheet">
<style>
:root{
  --navy:#082c50;
  --navy-mid:#123a73;
  --navy-foot:#163f80;
  --orange:#e77817;
  --orange-hi:#f26a1b;
  --text:#777;
  --text-dark:#555;
  --line:#c9c9c9;
  --panel:#eeeeee;
}
*{box-sizing:border-box;margin:0;padding:0}
html,body{width:1200px;height:1200px;overflow:hidden;background:#fff}
body{position:relative;font-family:"Source Sans 3",sans-serif;color:var(--text)}
.abs{position:absolute}
.head-font{font-family:"Ubuntu",sans-serif}

/* header */
.brand{left:228px;top:30px}
.brand-name{display:flex;align-items:center;gap:8px;font-size:23px;color:var(--navy);letter-spacing:.5px}
.brand-mark{width:20px;height:20px;border:2px solid var(--navy)}
.brand-url{font-size:8px;letter-spacing:5px;color:var(--navy);margin-top:6px;margin-left:18px}
.social{display:flex;gap:3px}
.social span{width:18px;height:18px;background:var(--navy-mid);border-radius:2px;display:block}
.social-top{left:918px;top:26px}
.search{left:811px;top:55px;width:190px;height:26px;border:1px solid #ccc;font-size:9px;color:#aaa;padding:7px 3px}
.search svg{position:absolute;right:5px;top:4px}

.nav{left:200px;top:93px;width:801px;height:29px;background:var(--navy);display:flex}
.nav a{color:#fff;text-decoration:none;font-family:"Arimo",sans-serif;font-size:12px;font-weight:700;display:flex;align-items:center;justify-content:center;border-right:1px solid #1d4478}
.nav a:last-child{border:0}

/* slider */
.slider{left:200px;top:132px;width:801px;height:280px;border:4px solid #c8c8c8;background:linear-gradient(90deg,#fff 0%,#efefef 100%)}
.slider-photo{left:4px;top:32px;width:396px;height:240px;background:linear-gradient(135deg,#dfe3ea 0%,#c7cfdc 45%,#8e8e93 100%)}
.slider h1{left:406px;top:40px;font-weight:400;font-size:41px;color:var(--navy);letter-spacing:-.5px;white-space:nowrap}
.slider h2{right:86px;top:87px;font-weight:400;font-size:20px;color:var(--navy)}
.slider h1 em{font-style:normal;color:var(--orange)}
.slider p{left:406px;top:114px;width:320px;font-size:11px;line-height:16px;color:var(--text)}
.btn-click{left:406px;top:168px;width:100px;height:30px;background:var(--orange-hi);color:#fff;font-size:16px;font-weight:600;display:flex;align-items:center;justify-content:center;border:1px solid #fbb07b}
.dots{left:714px;top:258px;display:flex;gap:3px}
.dots span{width:10px;height:10px;border-radius:50%;background:var(--navy)}
.dots span.on{background:var(--orange-hi)}

/* welcome */
.welcome-title{left:200px;top:434px;font-size:24px;font-weight:600;color:var(--navy);letter-spacing:-.3px}
.welcome-title em{font-style:normal;color:var(--orange)}
.welcome-text{left:200px;top:470px;width:565px;font-size:11px;line-height:17.6px}
.btn{height:23px;color:#fff;font-size:10.5px;display:flex;align-items:center;justify-content:center}
.btn-navy{background:var(--navy)}
.btn-orange{background:var(--orange-hi);border:1px solid #fbb07b}
.rule{border-top:1px dotted #aaa}
.vrule{left:779px;top:443px;height:490px;border-left:1px dashed #bbb}

/* services */
.svc-head{top:672px;width:179px;height:29px;color:#fff;font-size:14px;font-weight:500;display:flex;align-items:center;justify-content:center}
.svc-text{top:716px;width:170px;font-family:"Arimo",sans-serif;font-size:9.6px;line-height:14.4px;color:var(--text-dark)}
.svc-photo{top:806px;width:179px;height:94px;border:2px solid #ddd;box-shadow:0 6px 6px -4px #aaa}

/* sidebar */
.app{left:800px;top:441px;width:202px;height:149px;background:linear-gradient(#e8e8e8,#f1f1f1);border:1px solid #d4d4d4;text-align:center}
.app-mark{width:34px;height:34px;border:2px solid var(--navy);margin:12px auto 0}
.app h3{font-weight:500;font-size:19px;color:var(--navy);margin-top:14px}
.app .btn-dl{width:114px;height:26px;margin:4px auto 0;background:var(--orange-hi);color:#fff;font-size:16px;font-weight:600;display:flex;align-items:center;justify-content:center;border:1px solid #fbb07b}
.app p{font-size:9.5px;color:#555;margin-top:7px}

.news{left:800px;top:597px;width:202px;height:335px;border:1px solid #ccc}
.news-head{height:32px;background:var(--navy);display:flex;align-items:center;justify-content:space-between;padding:0 6px}
.news-head h3{color:#fff;font-weight:600;font-size:15px}
.news-head span{color:#fff;font-size:9px}
.news-item{position:absolute;left:7px;width:187px;display:flex;gap:6px}
.news-item .thumb{width:50px;height:50px;background:linear-gradient(135deg,#d9dee8,#9aa6b8);border:1px solid #ccc;flex:none}
.news-item .date{font-size:13px;color:var(--navy)}
.news-item p{font-size:8.5px;line-height:11.5px;color:#777}
.news-item a{font-size:9px;color:var(--navy);text-decoration:none}
.news-sep{position:absolute;left:7px;width:187px;border-top:1px dotted #999}

/* footer */
.footer{left:0;top:970px;width:1200px;height:230px;background:var(--navy-foot);color:#fff}
.footer h4{position:absolute;top:19px;font-size:14.5px;font-weight:600;color:#fff}
.footer h4 em{font-style:normal;color:var(--orange-hi)}
.fsep{position:absolute;top:18px;height:156px;border-left:1px solid #2e5b9e}
.quote{position:absolute;font-size:26px;font-weight:700;color:var(--orange-hi);font-style:italic;line-height:1}
.testimonial{position:absolute;left:209px;top:77px;width:240px;font-size:8.8px;line-height:11.6px}
.form label{position:absolute;font-size:8.5px}
.form .field{position:absolute;left:552px;width:220px;height:26px;background:#1e4a97;border:1px solid #2a57a5}
.subscribe{position:absolute;left:553px;top:145px;width:84px;height:21px;background:var(--orange-hi);color:#fff;font-size:10px;display:flex;align-items:center;justify-content:center}
.contact{position:absolute;left:874px;top:52px;font-size:9.5px;line-height:17.5px}
.social-foot{position:absolute;left:874px;top:107px}
.social-foot span{background:#3d6cb8}
.copy{position:absolute;left:201px;top:189px;font-size:8px}
</style>
</head>
<body>

<header>
  <div class="abs brand">
    <div class="brand-name head-font"><span class="brand-mark"></span>MARLOW TESSING</div>
    <div class="brand-url">www.kavilora.com.au</div>
  </div>
  <div class="abs social social-top" aria-label="Social media links">
    <span></span><span></span><span></span><span></span>
  </div>
  <div class="abs search">Enter the keyword to search
    <svg width="17" height="17" viewBox="0 0 17 17"><circle cx="7" cy="7" r="5" fill="none" stroke="#e77817" stroke-width="2"/><line x1="10.5" y1="10.5" x2="15" y2="15" stroke="#e77817" stroke-width="2.5"/></svg>
  </div>
  <nav class="abs nav">
    <a style="width:115px">Home</a>
    <a style="width:123px">Services</a>
    <a style="width:149px">Case Studies</a>
    <a style="width:145px">Our Process</a>
    <a style="width:126px">About us</a>
    <a style="width:143px">Contact Us</a>
  </nav>
</header>

<section class="abs slider">
  <div class="abs slider-photo" role="img" aria-label="Stressed businesswoman at a desk beside a tall stack of overflowing binders"></div>
  <h1 class="abs"><em>HAVE</em> PROBLEMS?</h1>
  <h2 class="abs">We Have Solution</h2>
  <p class="abs">Lorem ipsum dolor sit amet, consectetuer adipiscing elit, s diam nonummy nibh euismod tincidunt ut laoreet dolore maba dolore aliquam erat volutpat. Ut wisi enim ad minim veniam,</p>
  <div class="abs btn-click">Click Here</div>
  <div class="abs dots"><span></span><span></span><span></span><span class="on"></span><span></span></div>
</section>

<main>
  <h2 class="abs welcome-title">WELCOME TO MARLOW <em>TESSING</em></h2>
  <p class="abs welcome-text">Lorem ipsum dolor sit amet, consectetuer adipiscing elit, sed diam nonummy nibh euismod tincidunt ut laoreet dolore magna aliquam erat volutpat. Ut wisi enim ad minim veniam, quis nostrud exerci tation ullamcorper suscipit lobortis nisl ut aliquip ex ea commodo consequat. Duis autem vel eum iriure dolor in hendrerit in vulputate velit esse molestie consequat, vel illum dolore eu feugiat nulla facilisis at vero eros et accumsan et iusto odio dignissim qui nibh euismod tincidunt ut laoreet dolore magna aliquam erat volutpat. Ut wisi enim ad minim veniam, quis nostrud exerci tation ullamcorper suscipit lobortis nisl ut aliquip ex ea commodo consequat. Duis autem vel eum iriure dolor in hendrerit in vulputate velit esse molestie consequa.</p>
  <div class="abs btn btn-navy" style="left:200px;top:607px;width:89px">READ MORE</div>
  <div class="abs rule" style="left:200px;top:650px;width:565px"></div>
  <div class="abs vrule"></div>

  <div class="abs svc-head head-font" style="left:200px;background:var(--navy)">Facilitation</div>
  <div class="abs svc-head head-font" style="left:391px;background:var(--orange-hi);border:1px solid #fbb07b">Conflict Coaching</div>
  <div class="abs svc-head head-font" style="left:582px;background:var(--navy)">Negotiation</div>

  <p class="abs svc-text" style="left:205px">Lorem ipsum dolor sit amet, cectetuer adipiscing elit, sed diam nommy nibh euismod tincidunt ut laoreet dore magna aliquam erat volutpat, quis nostrud exerci tation ullamcorper.</p>
  <p class="abs svc-text" style="left:395px">Lorem ipsum dolor sit amet, cectetuer adipiscing elit, sed diam nommy nibh euismod tincidunt ut laoreet dore magna aliquam erat volutpat, quis nostrud exerci tation ullamcorper.</p>
  <p class="abs svc-text" style="left:588px">Lorem ipsum dolor sit amet, cectetuer adipiscing elit, sed diam nommy nibh euismod tincidunt ut laoreet dore magna aliquam erat volutpat, quis nostrud exerci tation ullamcorper.</p>

  <div class="abs svc-photo" style="left:200px;background:linear-gradient(135deg,#f2f2f2,#b9b9b9 60%,#555)" role="img" aria-label="Facilitator presenting at a flip chart to a seated group"></div>
  <div class="abs svc-photo" style="left:391px;background:linear-gradient(135deg,#e9eef5,#c3ccd8 55%,#4a5566)" role="img" aria-label="Two professionals in discussion across a table with a laptop"></div>
  <div class="abs svc-photo" style="left:584px;background:linear-gradient(135deg,#dde3ea,#8b95a3 55%,#2f3540)" role="img" aria-label="Business people shaking hands after a negotiation"></div>

  <div class="abs btn btn-orange" style="left:294px;top:914px;width:84px;height:21px">READ MORE</div>
  <div class="abs btn btn-navy" style="left:485px;top:914px;width:84px;height:21px">READ MORE</div>
  <div class="abs btn btn-orange" style="left:678px;top:914px;width:84px;height:21px">READ MORE</div>
</main>

<aside>
  <div class="abs app">
    <div class="app-mark"></div>
    <h3>TRY OUR APP</h3>
    <div class="btn-dl">Download</div>
    <p>Click here to free download.</p>
  </div>

  <div class="abs news">
    <div class="news-head"><h3>LATEST NEWS</h3><span>see more</span></div>
    <div class="news-item" style="top:41px"><div class="thumb" role="img" aria-label="Portrait of a businesswoman"></div><div><div class="date head-font">9-19-2013</div><p>Lorem ipsum dolor sit amet, consectetuer adipiscing elit, sed</p><a>read more</a></div></div>
    <div class="news-sep" style="top:103px"></div>
    <div class="news-item" style="top:114px"><div class="thumb" role="img" aria-label="Portrait of a businessman"></div><div><div class="date head-font">9-19-2013</div><p>Lorem ipsum dolor sit amet, consectetuer adipiscing elit, sed</p><a>read more</a></div></div>
    <div class="news-sep" style="top:177px"></div>
    <div class="news-item" style="top:190px"><div class="thumb" role="img" aria-label="Portrait of a businessman"></div><div><div class="date head-font">9-19-2013</div><p>Lorem ipsum dolor sit amet, consectetuer adipiscing elit, sed</p><a>read more</a></div></div>
    <div class="news-sep" style="top:256px"></div>
    <div class="news-item" style="top:268px"><div class="thumb" role="img" aria-label="Portrait of a businesswoman"></div><div><div class="date head-font">9-19-2013</div><p>Lorem ipsum dolor sit amet, consectetuer adipiscing elit, sed</p><a>read more</a></div></div>
  </div>
</aside>

<footer class="abs footer">
  <h4 class="head-font" style="left:203px">What Our Clients <em>Says</em></h4>
  <div class="quote" style="left:200px;top:54px">&#8220;</div>
  <p class="testimonial">Consectetuer adipiscing elit, sed diam nonummy nibh euismod tincidunt ut laoreet dolore magna aliquam erat volutpat. Ut wisi enim ad minim quis nostrud exerci tation ullamcorper suscipit lobortis nisl veniam, quis nostrud exerci tation ullamcorper suscipit lobortis nisl ut aliquip ex ea commodo consequat.</p>
  <div class="quote" style="left:432px;top:144px">&#8221;</div>
  <div class="fsep" style="left:497px"></div>

  <h4 class="head-font" style="left:551px">Monthly <em>Newsletter</em></h4>
  <div class="form">
    <label style="left:552px;top:52px">Name</label>
    <div class="field" style="top:63px"></div>
    <label style="left:552px;top:98px">Email</label>
    <div class="field" style="top:110px"></div>
  </div>
  <div class="subscribe">Subscribe</div>
  <div class="fsep" style="left:830px"></div>

  <h4 class="head-font" style="left:874px">Follow <em>Us</em></h4>
  <div class="contact">Phone: 1 300 555 0142<br>Fax: &nbsp;&nbsp;&nbsp;&nbsp;&nbsp;1 300 555 0143<br>Email: &nbsp;info@kavilora.com.au</div>
  <div class="social social-foot" aria-label="Social media links">
    <span></span><span></span><span></span><span></span>
  </div>

  <div class="copy">Copyright © 2013 kavilora.com.au . All Rights Reserved</div>
</footer>

</body>
</html>
```